Online Course Page

We are building a video based online course page. This project is for only the actual page that the student will watch the videos at. They will watch one vide at a time. Once one video lesson is completed then they can move to the next video lesson. The page will need to show the video player. (Main feature.) The list of lessons in the course. Instructor information. Profile picture and bio of the instructor. A Live chat button that will initiate a chat in real-time with the instructor.

The winning designer will also be asked to to design the dashboard area and other aspects of the user interface as an additional project.

Target Market(s)

Adults

Number of Pages Required

1 page

Colors
9bcb3c

Requirements
Must have
• Our logo is attached. Green and grey are our colors. Should feel modern, clean and be simple to navigate. The site will be responsive so the layout should work well on mobile devices.

```html
<!DOCTYPE html>
<html lang="en">
<head>
<meta charset="utf-8">
<title>LearnHarbor – Online Courses</title>
<link href="https://fonts.googleapis.com/css2?family=Poppins:wght@400;500;600&display=swap" rel="stylesheet">
<style>
:root{
  --green:#8cc63f;
  --green-dark:#6fa82a;
  --ink:#222;
  --text:#555;
  --muted:#888;
  --line:#e6e6e6;
  --price:#e2231a;
  --star:#f5b800;
  --band:#f3f3f3;
  --footer:#1d1d1d;
  --footer-text:#9a9a9a;
  --hero-a:#3a3550;
  --hero-b:#6b5a6e;
}
*{box-sizing:border-box;margin:0;padding:0}
html,body{width:753px;height:1200px;overflow:hidden;background:#fff}
body{position:relative;font-family:'Poppins',sans-serif;color:var(--ink)}
.abs{position:absolute}
/* header */
.site-header{position:absolute;left:0;top:0;width:753px;height:47px;background:#fff}
.brand{position:absolute;left:136px;top:14px;display:flex;align-items:center;gap:6px;font-size:13px;font-weight:600;color:var(--green-dark)}
.brand-dot{width:18px;height:18px;border-radius:50%;background:var(--green)}
.main-nav a{position:absolute;top:19px;font-size:6.5px;color:#444;text-decoration:none}
.search{position:absolute;left:498px;top:17px;width:80px;height:14px;border:1px solid #ddd;border-radius:7px;font-size:5.5px;color:#aaa;padding:3px 0 0 14px}
.search svg{position:absolute;left:4px;top:3px}
.icon-btn{position:absolute;top:16px;width:15px;height:15px;border-radius:50%}
/* hero */
.hero{position:absolute;left:0;top:47px;width:753px;height:274px;background:linear-gradient(120deg,var(--hero-b),var(--hero-a) 55%,#2a2f45)}
.play{position:absolute;left:346px;top:107px}
.play-label{position:absolute;left:0;width:753px;top:174px;text-align:center;color:#fff;font-size:8px;font-weight:500}
/* columns */
.section-title{position:absolute;font-size:11px;font-weight:500;color:var(--ink)}
.row{position:absolute;height:63px;border-bottom:1px solid var(--line)}
.thumb{position:absolute;left:0;top:0;width:59px;height:40px}
.course-title{position:absolute;left:69px;top:-1px;width:165px;font-size:7px;line-height:10.5px;color:#333}
.price{position:absolute;left:69px;top:28px;font-size:7px;font-weight:500;color:var(--price)}
.rating{position:absolute;left:120px;top:29px;font-size:4.3px;color:#777;display:flex;align-items:center;gap:3px;text-transform:uppercase}
.stars{color:var(--star);font-size:6px;letter-spacing:1px}
.avatar{position:absolute;left:0;top:0;width:39px;height:39px}
.inst-name{position:absolute;left:49px;top:-1px;font-size:7px;color:#333}
.inst-role{position:absolute;left:49px;top:10px;font-size:4.2px;color:#777;text-transform:uppercase}
.inst-bio{position:absolute;left:49px;top:18px;width:180px;font-size:5.6px;line-height:10px;color:#777}
.chat{position:absolute;left:178px;top:2px;width:45px;height:11px;border-radius:6px;background:var(--green);color:#fff;font-size:4.3px;text-transform:uppercase;display:flex;align-items:center;justify-content:center;gap:2px}
.show-all{position:absolute;top:690px;font-size:6.8px;color:#333;display:flex;align-items:center;gap:4px}
.divider{position:absolute;left:376px;top:352px;width:1px;height:356px;background:var(--line)}
/* testimonials */
.testimonials{position:absolute;left:0;top:740px;width:753px;height:202px;background:var(--band)}
.quote{position:absolute;left:189px;top:63px;width:376px;text-align:center;font-size:5.8px;line-height:11px;color:#666}
.pager{position:absolute;top:80px;font-size:5.5px;letter-spacing:1.5px}
/* cta */
.cta{position:absolute;left:0;top:942px;width:753px;height:103px;background:linear-gradient(90deg,#3d4a66,#4a5670 40%,#3a4560)}
.cta h2{position:absolute;left:0;width:753px;top:25px;text-align:center;color:#fff;font-size:13.5px;font-weight:500}
.cta-btn{position:absolute;left:340px;top:52px;width:74px;height:19px;border-radius:10px;background:var(--green);color:#fff;font-size:6.8px;display:flex;align-items:center;justify-content:center}
/* footer */
.site-footer{position:absolute;left:0;top:1045px;width:753px;height:155px;background:var(--footer)}
.f-title{position:absolute;top:22px;color:#eee;font-size:7.5px;font-weight:500}
.f-text{position:absolute;top:40px;font-size:5.6px;line-height:11px;color:var(--footer-text)}
.social{position:absolute;left:460px;top:40px;display:flex;gap:4px}
.social span{width:16px;height:16px;background:#cfcfcf}
.copy{position:absolute;left:0;width:753px;top:116px;text-align:center;font-size:5.6px;color:var(--footer-text)}
</style>
</head>
<body>
<header class="site-header">
  <div class="brand"><span class="brand-dot"></span>LearnHarbor</div>
  <nav class="main-nav">
    <a style="left:299px">Courses</a><a style="left:336px">Instructors</a><a style="left:380px">Articles</a><a style="left:414px">About</a><a style="left:445px">Contact</a>
  </nav>
  <div class="search"><svg width="7" height="7" viewBox="0 0 10 10"><circle cx="4" cy="4" r="3" fill="none" stroke="#999" stroke-width="1.3"/><path d="M6.3 6.3 9 9" stroke="#999" stroke-width="1.3"/></svg>Enter search</div>
  <div class="icon-btn" style="left:586px;border:1.2px solid var(--green)"><svg width="13" height="13" viewBox="0 0 13 13"><circle cx="6.5" cy="5" r="2" fill="var(--green)"/><path d="M3 10c.6-2 6.4-2 7 0z" fill="var(--green)"/></svg></div>
  <div class="icon-btn" style="left:603px;border:1.2px solid #444"><svg width="13" height="13" viewBox="0 0 13 13"><path d="M3.5 5h6l-.8 4h-4.4z" fill="#444"/></svg></div>
</header>

<section class="hero" role="img" aria-label="Photo of a person typing on a laptop showing an online learning login screen">
  <svg class="play" width="60" height="60" viewBox="0 0 60 60"><circle cx="30" cy="30" r="30" fill="#fff" fill-opacity=".15"/><circle cx="30" cy="30" r="22" fill="#fff" fill-opacity=".2"/><circle cx="30" cy="30" r="12" fill="none" stroke="#fff" stroke-width="2"/><path d="M27 24.5v11l8.5-5.5z" fill="#fff"/></svg>
  <div class="play-label">Play &amp; Watch</div>
</section>

<h2 class="section-title" style="left:135px;top:350px">Our Online Courses</h2>
<div class="row" style="left:135px;top:374px;width:224px"><div class="thumb" role="img" aria-label="Desk flat lay photo" style="background:#7fa3c4"></div><p class="course-title">Professional lorem ipsum used generators for typographers</p><span class="price">$299.99</span><span class="rating"><span class="stars">★★★★★</span>(5 reviews) 36 students</span></div>
<div class="row" style="left:135px;top:437px;width:224px"><div class="thumb" role="img" aria-label="Classroom photo" style="background:#4d5a78"></div><p class="course-title">Professional lorem ipsum used generators for typographers</p><span class="price">$299.99</span><span class="rating"><span class="stars">★★★★★</span>(5 reviews) 36 students</span></div>
<div class="row" style="left:135px;top:500px;width:224px"><div class="thumb" role="img" aria-label="Students at computers photo" style="background:#b9aea4"></div><p class="course-title">Professional lorem ipsum used generators for typographers</p><span class="price">$299.99</span><span class="rating"><span class="stars">★★★★★</span>(5 reviews) 36 students</span></div>
<div class="row" style="left:135px;top:563px;width:224px"><div class="thumb" role="img" aria-label="E-learning icons illustration" style="background:#e4e7ea"></div><p class="course-title">Professional lorem ipsum used generators for typographers</p><span class="price">$299.99</span><span class="rating"><span class="stars">★★★★★</span>(5 reviews) 36 students</span></div>
<div class="row" style="left:135px;top:626px;width:224px;border-bottom:none"><div class="thumb" role="img" aria-label="Laptop with digital network photo" style="background:#1f4f8c"></div><p class="course-title">Professional lorem ipsum used generators for typographers</p><span class="price">$299.99</span><span class="rating"><span class="stars">★★★★★</span>(5 reviews) 36 students</span></div>
<div class="show-all" style="left:216px">Show All Courses <svg width="10" height="5" viewBox="0 0 10 5"><path d="M0 2.5h9M6.5 .5 9 2.5 6.5 4.5" fill="none" stroke="#333" stroke-width=".8"/></svg></div>

<div class="divider"></div>

<h2 class="section-title" style="left:394px;top:350px">Our Instructors</h2>
<div class="row" style="left:394px;top:376px;width:224px"><div class="avatar" role="img" aria-label="Instructor portrait" style="background:#c9ced6"></div><span class="inst-name">William doe</span><span class="inst-role">Courses by instructor</span><p class="inst-bio">lorem ipsum is a placeholder text commonly place used to demonstrate the visual.</p><span class="chat">● Live chat</span></div>
<div class="row" style="left:394px;top:437px;width:224px"><div class="avatar" role="img" aria-label="Instructor portrait" style="background:#d8cbbf"></div><span class="inst-name">Sofia Khnna</span><span class="inst-role">Courses by instructor</span><p class="inst-bio">lorem ipsum is a placeholder text commonly place used to demonstrate the visual.</p><span class="chat">● Live chat</span></div>
<div class="row" style="left:394px;top:501px;width:224px"><div class="avatar" role="img" aria-label="Instructor portrait" style="background:#cfd3d8"></div><span class="inst-name">John Smith</span><span class="inst-role">Courses by instructor</span><p class="inst-bio">lorem ipsum is a placeholder text commonly place used to demonstrate the visual.</p><span class="chat">● Live chat</span></div>
<div class="row" style="left:394px;top:565px;width:224px"><div class="avatar" role="img" aria-label="Instructor portrait" style="background:#8a7060"></div><span class="inst-name">Casoline</span><span class="inst-role">Courses by instructor</span><p class="inst-bio">lorem ipsum is a placeholder text commonly place used to demonstrate the visual.</p><span class="chat">● Live chat</span></div>
<div class="row" style="left:394px;top:629px;width:224px"><div class="avatar" role="img" aria-label="Instructor portrait" style="background:#c3c9d1"></div><span class="inst-name">Tornado C</span><span class="inst-role">Courses by instructor</span><p class="inst-bio">lorem ipsum is a placeholder text commonly place used to demonstrate the visual.</p><span class="chat">● Live chat</span></div>
<div class="show-all" style="left:470px">Show All Instructors <svg width="10" height="5" viewBox="0 0 10 5"><path d="M0 2.5h9M6.5 .5 9 2.5 6.5 4.5" fill="none" stroke="#333" stroke-width=".8"/></svg></div>

<section class="testimonials">
  <h2 class="section-title" style="left:0;width:753px;text-align:center;top:28px;font-size:12px">Testimonials</h2>
  <p class="quote">"Morbi accumsan ipsum velit. Nam nec tellus a odio tincidunt auctor a ornare odio. Sed non mauris vitae erat consequat auctor eu in elit. Class aptent taciti sociosqu ad litora torquent per conubia nostra, per inceptos himenaeos. Mauris in erat justo. eu in elit. Class aptent taciti sociosqu ad litora torquent per conubia nostra, per inceptos himenaeos. Mauris in erat justo. Nullam ac condimentum sit amet a augue. Sed non neque elit. Sed ut imperdiet nisi. Proin nisl quis neque. Suspendisse in orci enim."</p>
  <div class="pager" style="left:64px;color:#444"><span style="margin-left:11px">PREV</span><svg class="abs" style="left:0;top:6px" width="32" height="8" viewBox="0 0 32 8"><path d="M5 1 1 4 5 7M1 4h30" fill="none" stroke="#444" stroke-width=".9"/></svg></div>
  <div class="pager" style="left:658px;color:var(--price)"><span>NEXT</span><svg class="abs" style="left:0;top:6px" width="32" height="8" viewBox="0 0 32 8"><path d="M27 1 31 4 27 7M0 4h31" fill="none" stroke="var(--price)" stroke-width=".9"/></svg></div>
  <div class="abs" role="img" aria-label="Reviewer portrait" style="left:325px;top:131px;width:38px;height:38px;border-radius:50%;background:#c8c8c8;border:2px solid #fff"></div>
  <span class="abs" style="left:372px;top:133px;font-size:7.5px;color:#333">William Doe</span>
  <span class="abs" style="left:372px;top:145px;font-size:5.6px;color:#777">Dolor sit amet</span>
  <span class="abs stars" style="left:372px;top:155px;font-size:7px">★★★★★</span>
</section>

<section class="cta" role="img" aria-label="Photo of students sitting with laptops and tablets">
  <h2>Join and Start the online learning today!</h2>
  <span class="cta-btn">Join us today!</span>
</section>

<footer class="site-footer">
  <h3 class="f-title" style="left:146px">About LearnHarbor</h3>
  <p class="f-text" style="left:146px;width:150px">Class aptent taciti sociosqu ad litora torquent per conubia nostra, per inceptos himenaeos. Mauris in erat justo. Nullam ac condimentum sit amet a augue.</p>
  <h3 class="f-title" style="left:342px">Course Categories</h3>
  <p class="f-text" style="left:342px">lorem ipsum dolor sit 01<br>lorem ipsum dolor sit 02<br>lorem ipsum dolor sit 03<br>lorem ipsum dolor sit 04</p>
  <h3 class="f-title" style="left:460px">Stay Connected</h3>
  <div class="social"><span></span><span></span><span></span><span></span><span></span></div>
  <p class="copy">Copyright © 2018 All Rights Reserved.</p>
</footer>
</body>
</html>
```